T Varlo

Ned a new business card, need two designs one to be for communications and one to be for security.
Communications will have what we do on it which include:-
PABX systems
Data Cabling
Phone services
Fibre
Security
"your communications specialist in the Pilbara"
The Severity one will have on it:-
CCTV
Alarm
Access control
Security consulting
Communications services
"Your security partner in the Pilbara"
Target Market(s)
industry
Industry/Entity Type
Communications
Contact Information for Business Card
Marcus Delby
0493726051
marcus@tvarlo.com.au
www.tvarlo.com.au

```html
<!DOCTYPE html>
<html lang="en">
<head>
<meta charset="utf-8">
<title>T Varlo business cards</title>
<link href="https://fonts.googleapis.com/css2?family=Open+Sans:wght@400;600;700&display=swap" rel="stylesheet">
<style>
  :root {
    --backdrop: #d6d6d6;
    --card: #ffffff;
    --band: #f2b65c;
    --band-deep: #e9a94b;
    --accent: #eeab48;
    --ink: #6b6b6b;
    --mark: #7a7a7a;
  }
  * { margin: 0; padding: 0; box-sizing: border-box; }
  html, body { width: 1200px; height: 742px; overflow: hidden; }
  body {
    background: var(--backdrop);
    font-family: "Open Sans", Arial, sans-serif;
    position: relative;
  }
  .card {
    position: absolute;
    top: 201px;
    width: 560px;
    height: 340px;
    background: var(--card);
    box-shadow: 0 6px 18px rgba(0,0,0,0.18);
    overflow: hidden;
  }
  .card--security { left: 27px; }
  .card--communications { left: 613px; }
  .band { position: absolute; background: var(--band); }
  .band--top { left: 48%; right: 0; top: 40px; height: 36px; }
  .band--tagline { left: 30%; right: 0; top: 92px; height: 22px; }
  .band--mid { left: 0; width: 50%; top: 130px; height: 20px; background: var(--band-deep); }
  .band--name { left: 0; width: 47%; top: 164px; height: 46px; background: var(--band-deep); }
  .tagline {
    position: absolute; left: 12px; top: 3px;
    color: #fff; font-size: 11px; letter-spacing: 2.2px; white-space: nowrap;
  }
  .brand {
    position: absolute; left: 26px; top: 46px;
    display: flex; align-items: center; gap: 10px;
  }
  .brand__dot { width: 22px; height: 22px; border-radius: 50%; background: var(--mark); }
  .brand__name { color: var(--accent); font-size: 38px; font-weight: 700; line-height: 1; }
  .person {
    position: absolute; left: 26px; top: 6px;
    color: #fff; font-size: 26px; font-weight: 600; white-space: nowrap;
  }
  .contact {
    position: absolute; left: 26px; top: 238px;
    color: var(--ink); font-size: 15px; line-height: 21px; letter-spacing: 0.4px;
  }
  .services {
    position: absolute; left: 316px; top: 140px; list-style: none;
    color: var(--accent); font-size: 17px; line-height: 28px;
  }
  .services li { display: flex; align-items: center; gap: 8px; white-space: nowrap; }
  .services svg { width: 12px; height: 12px; flex: none; }
</style>
</head>
<body>

<div class="card card--security">
  <div class="band band--top"></div>
  <div class="band band--tagline"><span class="tagline">Your security partner in the Pilbara</span></div>
  <div class="brand"><span class="brand__dot"></span><span class="brand__name">T Varlo</span></div>
  <div class="band band--mid"></div>
  <div class="band band--name"><span class="person">Marcus Delby</span></div>
  <ul class="services">
    <li><svg viewBox="0 0 12 12"><path d="M1 6.5 L4.5 10 L11 2" fill="none" stroke="currentColor" stroke-width="2.4"/></svg>CCTV</li>
    <li><svg viewBox="0 0 12 12"><path d="M1 6.5 L4.5 10 L11 2" fill="none" stroke="currentColor" stroke-width="2.4"/></svg>Alarm</li>
    <li><svg viewBox="0 0 12 12"><path d="M1 6.5 L4.5 10 L11 2" fill="none" stroke="currentColor" stroke-width="2.4"/></svg>Access control</li>
    <li><svg viewBox="0 0 12 12"><path d="M1 6.5 L4.5 10 L11 2" fill="none" stroke="currentColor" stroke-width="2.4"/></svg>Security consulting</li>
    <li><svg viewBox="0 0 12 12"><path d="M1 6.5 L4.5 10 L11 2" fill="none" stroke="currentColor" stroke-width="2.4"/></svg>Communications services</li>
  </ul>
  <div class="contact">
    <p>0493726051</p>
    <p>marcus@tvarlo.com.au</p>
    <p>www.tvarlo.com.au</p>
  </div>
</div>

<div class="card card--communications">
  <div class="band band--top"></div>
  <div class="band band--tagline"><span class="tagline">Your communications specialist in the Pilbara</span></div>
  <div class="brand"><span class="brand__dot"></span><span class="brand__name">T Varlo</span></div>
  <div class="band band--mid"></div>
  <div class="band band--name"><span class="person">Marcus Delby</span></div>
  <ul class="services">
    <li><svg viewBox="0 0 12 12"><path d="M1 6.5 L4.5 10 L11 2" fill="none" stroke="currentColor" stroke-width="2.4"/></svg>PABX systems</li>
    <li><svg viewBox="0 0 12 12"><path d="M1 6.5 L4.5 10 L11 2" fill="none" stroke="currentColor" stroke-width="2.4"/></svg>Data Cabling</li>
    <li><svg viewBox="0 0 12 12"><path d="M1 6.5 L4.5 10 L11 2" fill="none" stroke="currentColor" stroke-width="2.4"/></svg>Phone services</li>
    <li><svg viewBox="0 0 12 12"><path d="M1 6.5 L4.5 10 L11 2" fill="none" stroke="currentColor" stroke-width="2.4"/></svg>Fibre</li>
    <li><svg viewBox="0 0 12 12"><path d="M1 6.5 L4.5 10 L11 2" fill="none" stroke="currentColor" stroke-width="2.4"/></svg>Security</li>
  </ul>
  <div class="contact">
    <p>0493726051</p>
    <p>marcus@tvarlo.com.au</p>
    <p>www.tvarlo.com.au</p>
  </div>
</div>

</body>
</html>
```